Beauty Supplier from Europe needs a packaging design for cosmetics

We need a label design for Aloe Vera bottles. The bottles are clear. See attached file.
Label Size: 146 x 105 mm (Width x Height)
Peel back label is possible.
Brand logo is suvetta. Logo is attached.
We need open Adobe InDesign or Adobe Illustrator files including graphics, photos and fonts.
Aloe Vera
Gentle, Soothing, Cooling
Fragrance Free
200 g
99,9% Aloe Vera
Directions: Apply to clean dry skin. Washing hands before and after use.
Ingredients: Barbadens Leafe Extract, Citric Acid, Sodium Benzoate, Potassium sorbate
Warning: For external use only. Keep out of reach of children.
Responsible Person
Batch code - see attached file
Open jar symbol - see attached file
German translation
Aloe Vera
sanft - beruhigend - kühlend
Parfümfrei
Anwendung: Auf die gereinigte trockene Haut auftragen. Reinigen Sie Ihre Hände vor und nach der Anwendung.
Warnhinweise: Nur zur äußeren Anwendung. Darf nicht in die Hände von Kindern gelangen.
We need also French and Dutch translation. Please use dummy text.
Target Market(s)
Afro-American and European women
Industry/Entity Type
Cosmetics
Colors
Designer to choose colors to be used in the design.
Look and feel

```html
<!DOCTYPE html>
<html lang="en">
<head>
<meta charset="utf-8">
<title>Suvetta Aloe Vera Label</title>
<link rel="stylesheet" href="https://fonts.googleapis.com/css2?family=Marcellus+SC&family=Open+Sans:ital,wght@0,400;0,600;1,400&display=swap">
<style>
  :root {
    --backdrop: #e0d4c7;
    --leaf-dark: #5cae47;
    --leaf-mid: #73bb4b;
    --leaf-light: #b2cc3c;
    --leaf-lime: #a6c83a;
    --cream: #ffffff;
    --photo-deep: #4f5a3b;
    --photo-skin: #d9b8a4;
    --photo-green: #8fae6a;
  }
  html, body {
    margin: 0;
    padding: 0;
    width: 1200px;
    height: 900px;
    overflow: hidden;
    background: var(--backdrop);
  }
  .canvas {
    position: relative;
    width: 1200px;
    height: 900px;
    display: flex;
    align-items: center;
    justify-content: center;
  }
  .label {
    position: relative;
    width: 352px;
    height: 840px;
    overflow: hidden;
    background: var(--leaf-dark);
  }
  .label-photo {
    position: absolute;
    inset: 0 0 260px 0;
    background:
      radial-gradient(ellipse 60% 45% at 60% 35%, var(--photo-skin) 0%, rgba(217,184,164,0) 70%),
      linear-gradient(160deg, var(--photo-deep) 0%, var(--photo-green) 45%, #b9a08c 100%);
  }
  .label-art {
    position: absolute;
    inset: 0;
    width: 352px;
    height: 840px;
  }
  .label-base {
    position: absolute;
    left: 0;
    right: 0;
    bottom: 0;
    height: 200px;
    background: linear-gradient(180deg, rgba(166,200,58,0) 0%, var(--leaf-lime) 30%, var(--leaf-light) 100%);
  }
  .brand {
    position: absolute;
    top: 62px;
    left: 0;
    right: 0;
    display: flex;
    flex-direction: column;
    align-items: center;
    gap: 6px;
    color: var(--cream);
  }
  .brand-dot {
    width: 50px;
    height: 50px;
    border-radius: 50%;
    background: var(--cream);
  }
  .brand-name {
    font-family: "Open Sans", sans-serif;
    font-weight: 400;
    font-size: 26px;
    letter-spacing: 1px;
    line-height: 1;
  }
  .product-title {
    position: absolute;
    top: 518px;
    left: 52px;
    right: 52px;
    text-align: center;
    color: var(--cream);
    border-top: 1px solid rgba(255,255,255,0.55);
    border-bottom: 1px solid rgba(255,255,255,0.55);
    padding: 10px 0 10px;
  }
  .product-name {
    margin: 0;
    font-family: "Marcellus SC", serif;
    font-weight: 400;
    font-size: 50px;
    line-height: 1;
  }
  .product-claims {
    margin: 4px 0 0;
    font-family: "Open Sans", sans-serif;
    font-style: italic;
    font-size: 18px;
    line-height: 1.2;
  }
  .label-footer {
    position: absolute;
    left: 42px;
    right: 42px;
    bottom: 26px;
    display: flex;
    justify-content: space-between;
    font-family: "Open Sans", sans-serif;
    font-size: 13px;
    color: var(--cream);
  }
  .fragrance-note { font-weight: 600; }
  .net-weight { font-weight: 400; opacity: 0.9; }
</style>
</head>
<body>
<div class="canvas">
  <div class="label">
    <div class="label-photo" role="img" aria-label="Photo of a woman holding aloe vera gel in her hand beside aloe leaves"></div>

    <svg class="label-art" viewBox="0 0 352 840" aria-hidden="true">
      <defs>
        <linearGradient id="domeFill" x1="0" y1="0" x2="1" y2="1">
          <stop offset="0" stop-color="#5cae47"/>
          <stop offset="1" stop-color="#78bd4b"/>
        </linearGradient>
      </defs>
      <path class="dome" d="M0 520 Q176 340 352 520 V840 H0 Z" fill="url(#domeFill)"/>
    </svg>

    <div class="label-base" role="img" aria-label="Decorative wave band in white and lime green"></div>

    <div class="brand">
      <span class="brand-dot"></span>
      <span class="brand-name">suvetta</span>
    </div>

    <div class="product-title">
      <h1 class="product-name">Aloe Vera</h1>
      <p class="product-claims">Gentle, Soothing, Cooling</p>
    </div>

    <div class="label-footer">
      <span class="fragrance-note">Fragrance Free</span>
      <span class="net-weight">200 g</span>
    </div>
  </div>
</div>
</body>
</html>
```